Allied Health team of Physiotherapists & Occupational Therapists seek a business card design

We have our new logo, we now need our new business cards and stationary. Blossom: Lymphoedema & Women's Clinic is seeking a generic card design to represent our whole team and individual cards for each therapist that incorporates our new logo to communicate our holistic approach that is calming, nuturing, supportive and welcoming.
Our Physiotherapists and Occupational Therapists assess, treat and provide education for people who are at risk of or who have lymphoedema. This is often as a result of treatment for cancer. We provide pre-operative and post-operative management and cancer rehabilitation in our Pilates studio. Our team also consists of Physiotherapists who have a strong interest in pelvic floor and continence management for both men and women.

Target Market(s)

Mainly women health conscious

Industry/Entity Type

Allied Health: Physiotherapy / Occupational Therapy

Contact Information for Business Card

Address: 14 Calloway Ave Frankston 3199 Phone: 84317560 fax: 8431 7564 Email: info@blossomcarepartners.com.au Website: blossomcarepartners.com.au Facebook address: facebook.com/BlossomLymphoedemaAndWomensCareCentre. Room to write appointments. Individual cards need to have name, office email and individual email and professional details

Requirements
Must have
• Logo as per uploaded documents

```html
<!DOCTYPE html>
<html lang="en">
<head>
<meta charset="utf-8">
<title>Blossom: Lymphoedema &amp; Women's Clinic – Business Cards</title>
<link href="https://fonts.googleapis.com/css2?family=Cinzel:wght@700&family=Open+Sans:wght@400;600&display=swap" rel="stylesheet">
<style>
  :root {
    --page: #f3f3f3;
    --card-white: #ffffff;
    --peach: #f9b185;
    --peach-ink: #f4a473;
    --ink: #333333;
    --ink-dark: #111111;
    --on-peach: #ffffff;
  }
  * { margin: 0; padding: 0; box-sizing: border-box; }
  html, body {
    width: 1200px; height: 800px; overflow: hidden;
    background: var(--page);
    font-family: "Open Sans", Arial, sans-serif;
  }
  .canvas { position: relative; width: 1200px; height: 800px; }

  .card {
    position: absolute;
    width: 572px; height: 331px;
  }
  .card--front { left: 475px; top: 32px; background: var(--card-white); }
  .card--back  { left: 169px; top: 406px; background: var(--peach); }

  .person { position: absolute; left: 35px; top: 52px; }
  .person__name {
    font-family: "Cinzel", Georgia, serif;
    font-weight: 700; font-size: 19px; letter-spacing: 0.5px;
    color: var(--peach-ink); line-height: 1;
  }
  .person__role {
    font-size: 10px; color: var(--ink-dark); margin-left: 4px; margin-top: 1px;
  }

  .address {
    position: absolute; left: 35px; top: 132px;
    font-size: 14px; line-height: 20px; color: var(--ink);
  }

  .contacts { position: absolute; left: 35px; top: 209px; list-style: none; }
  .contacts li {
    display: flex; align-items: center; height: 25px;
    font-size: 14px; color: var(--ink);
  }
  .contacts svg { width: 17px; height: 17px; margin-right: 12px; flex: none; }

  .brand {
    position: absolute; display: flex; align-items: center; gap: 8px;
    font-family: "Open Sans", Arial, sans-serif; font-weight: 400;
  }
  .brand__dot { border-radius: 50%; flex: none; }
  .brand__text { line-height: 1.25; }

  .card--front .brand { left: 368px; top: 140px; color: var(--peach-ink); }
  .card--front .brand__dot { width: 12px; height: 12px; background: var(--peach-ink); }
  .card--front .brand__name { font-size: 30px; }
  .card--front .brand__tag { font-size: 9px; }

  .card--back .brand { left: 185px; top: 134px; color: var(--on-peach); }
  .card--back .brand__dot { width: 14px; height: 14px; background: var(--on-peach); }
  .card--back .brand__name { font-size: 36px; }
  .card--back .brand__tag { font-size: 10px; }
</style>
</head>
<body>
<main class="canvas">

  <section class="card card--front" aria-label="Business card front">
    <div class="person">
      <div class="person__name">CLARA WHITFIELD</div>
      <div class="person__role">CEO/Managing Director</div>
    </div>

    <p class="address">14 Calloway Ave<br>Suite 4, Frankston VIC 3199</p>

    <ul class="contacts">
      <li>
        <svg viewBox="0 0 20 20" aria-hidden="true">
          <path d="M5 2 L8 6 L6.5 8 Q8 11.5 12 13.5 L14 12 L18 15 L16 18 Q9 18 4.5 13 Q1.5 8.5 2.5 4 Z" fill="var(--peach-ink)"/>
          <path d="M12 3 A5 5 0 0 1 17 8 M12 6 A2 2 0 0 1 14 8" fill="none" stroke="var(--peach-ink)" stroke-width="1.3"/>
        </svg>
        8431 7560
      </li>
      <li>
        <svg viewBox="0 0 20 20" aria-hidden="true">
          <rect x="2" y="5" width="16" height="11" fill="var(--peach-ink)"/>
          <path d="M2 5 L10 11.5 L18 5" fill="none" stroke="#fff" stroke-width="1.2"/>
        </svg>
        clara@blossomcarepartners.com.au
      </li>
      <li>
        <svg viewBox="0 0 20 20" aria-hidden="true" fill="none" stroke="var(--peach-ink)" stroke-width="1.1">
          <circle cx="10" cy="10" r="8"/>
          <ellipse cx="10" cy="10" rx="3.5" ry="8"/>
          <path d="M2 10 H18 M3.5 6 H16.5 M3.5 14 H16.5"/>
        </svg>
        www.blossomcarepartners.com.au
      </li>
    </ul>

    <div class="brand">
      <span class="brand__dot"></span>
      <div class="brand__text">
        <div class="brand__name">Blossom</div>
        <div class="brand__tag">Lymphoedema &amp; Women's Clinic</div>
      </div>
    </div>
  </section>

  <section class="card card--back" aria-label="Business card back">
    <div class="brand">
      <span class="brand__dot"></span>
      <div class="brand__text">
        <div class="brand__name">Blossom</div>
        <div class="brand__tag">Lymphoedema &amp; Women's Clinic</div>
      </div>
    </div>
  </section>

</main>
</body>
</html>
```